Professional Lighting Providers - Web Design

We need a web design to showcase our ability to provide lighting design and equipment to those who are in need of lighting equipment.

Our 4 markets are:
Broadcasting - Public and Commercial
Education - ISD wide, and private schools
Government - National News, Chamber videos, Press Releases
Religious - Sermon Recording, etc.

We provide lighting products, design consultations(how lights are setup and such), and custom light work.

We want the home page to be setup in a way that someone in one of the 4 markets can drill down into the site. Meaning they are greeted on the home page with 4 large icons or pictures for each market and then they can go farther into the site. We also want a top navigation to be preset so people who are just looking for lighting can also browse our products.

Logo colors are not as they appear on our current website.
#383388 is our current logo color, please also see attachment of logo. In addition, we are just "Bright Harbor - Lighting Systems". We dropped the RJ7 out of our name so please don't use it in the concept.

Our Current Site is http://rj7-example.com/index.asp.
We don't have set colors but we know we do not want reds or yellows.

The design should be simple, not cluttered, and not artsy, not fun, but very serious.

Requirements
Must have
• Image banner/slider at the top that slides our 4 products.
Also need to have a form on the home page that will convert visitors to subscribers for a newsletter. Also on every page we want a form were people can send an email off to us asking questions.

```html
<!DOCTYPE html>
<html lang="en">
<head>
<meta charset="utf-8">
<title>Bright Harbor - Lighting Systems</title>
<link href="https://fonts.googleapis.com/css2?family=PT+Sans:wght@400;700&family=Arimo:wght@400&display=swap" rel="stylesheet">
<style>
:root{
  --navy:#1b1d66;
  --navy-deep:#16185a;
  --nav-top:#3a3794;
  --nav-bottom:#28257a;
  --brand:#383388;
  --heading:#37338a;
  --text:#333;
  --page:#f7f7f7;
  --lower:#eeeeee;
  --rule:#d6d6d6;
  --white:#fff;
}
*{margin:0;padding:0;box-sizing:border-box}
html,body{width:1200px;height:1041px;overflow:hidden}
body{position:relative;background:var(--page);font-family:"PT Sans",sans-serif;color:var(--text)}
.top-nav{position:absolute;left:0;top:0;width:1200px;height:34px;background:linear-gradient(var(--nav-top),var(--nav-bottom));display:flex;justify-content:center}
.top-nav a{color:var(--white);text-decoration:none;font-weight:700;font-size:13px;line-height:34px;padding:0 13px;border-left:1px solid rgba(0,0,0,.3)}
.top-nav a:first-child{border-left:none}
.brand{position:absolute;top:56px;left:0;width:1200px;text-align:center;color:var(--brand);font-weight:700;font-size:22px;line-height:24px;display:flex;justify-content:center;align-items:center;gap:8px}
.brand-dot{width:22px;height:22px;border-radius:50%;background:var(--brand)}
.brand small{display:block;font-size:15px;letter-spacing:2px}
.markets{position:absolute;top:145px;left:151px;display:flex;gap:13px}
.market{position:relative;width:215px;height:433px;background:linear-gradient(135deg,var(--navy),var(--navy-deep));border:2px solid var(--white);box-shadow:0 0 0 1px #ccc;color:var(--white);text-align:center}
.market h2{position:absolute;top:90px;width:100%;font-size:23px;font-weight:400;letter-spacing:.3px}
.market svg{position:absolute;top:150px;left:57px}
.market p{position:absolute;top:282px;width:100%;font-size:17px;line-height:19px;padding:0 4px}
.market .cta{position:absolute;top:412px;width:100%;font-size:11px;font-weight:700}
.lower{position:absolute;top:638px;left:0;width:1200px;height:403px;background:var(--lower);box-shadow:inset 0 6px 6px -4px rgba(0,0,0,.12)}
.lower h3{position:absolute;color:var(--heading);font-size:15px;font-weight:700}
.body-text{position:absolute;font-family:"Arimo",sans-serif;font-size:11.5px;line-height:17.2px;color:var(--text)}
.divider{position:absolute;left:770px;top:29px;width:1px;height:289px;background:var(--rule)}
.thumb{position:absolute;top:218px;width:96px;height:76px;border:1px solid #ccc;background:var(--white);padding:3px}
.thumb span{display:block;width:100%;height:100%}
.view-all{position:absolute;left:685px;top:250px;font-size:11px;font-weight:700;color:#222}
.email-field{position:absolute;left:807px;top:236px;width:231px;height:28px;border:1px solid #ccc;background:var(--white);font-family:"Arimo",sans-serif;font-size:12px;padding:0 7px;line-height:26px;color:#222}
.subscribe{position:absolute;left:873px;top:274px;width:100px;height:24px;background:var(--nav-top);color:var(--white);font-size:13px;font-weight:700;line-height:24px;padding-left:9px}
.subscribe::after{content:"";position:absolute;right:0;top:0;width:17px;height:24px;background:var(--nav-bottom)}
.subscribe i{position:absolute;right:5px;top:8px;border-left:7px solid var(--white);border-top:4px solid transparent;border-bottom:4px solid transparent;z-index:1}
.footer-rule{position:absolute;left:115px;top:361px;width:970px;height:1px;background:#d8d8d8}
.copyright{position:absolute;top:373px;width:1200px;text-align:center;font-size:11px;font-weight:700;color:#222}
</style>
</head>
<body>
<nav class="top-nav">
  <a href="#">Home</a><a href="#">Why Us?</a><a href="#">Resume</a><a href="#">Products</a><a href="#">Lighting Design/Quote Request</a><a href="#">About Us</a><a href="#">Latest News</a><a href="#">Manuals</a><a href="#">Technical</a><a href="#">Contact Us</a>
</nav>

<div class="brand"><span class="brand-dot"></span><div>Bright Harbor<small>Lighting Systems</small></div></div>

<section class="markets">
  <article class="market">
    <h2>BROADCASTING</h2>
    <svg width="100" height="100" viewBox="0 0 100 100" aria-hidden="true">
      <rect x="38" y="12" width="24" height="44" rx="12" fill="#fff"/>
      <path d="M30 40v6a20 20 0 0 0 40 0v-6" fill="none" stroke="#fff" stroke-width="5"/>
      <rect x="46" y="66" width="8" height="14" fill="#fff"/>
    </svg>
    <p>Public and Commercial</p>
    <div class="cta">CLICK TO VIEW CATEGORY</div>
  </article>
  <article class="market">
    <h2>EDUCATION</h2>
    <svg width="100" height="100" viewBox="0 0 100 100" aria-hidden="true">
      <polygon points="0,38 52,20 104,38 52,56" fill="#fff"/>
      <path d="M24 48v18c12 8 44 8 56 0V48L52 58Z" fill="#fff"/>
      <path d="M90 42v26" stroke="#fff" stroke-width="2"/>
      <rect x="86" y="66" width="8" height="12" fill="#fff"/>
    </svg>
    <p>ISD wide, &amp; private schools</p>
    <div class="cta">CLICK TO VIEW CATEGORY</div>
  </article>
  <article class="market">
    <h2>GOVERNMENT</h2>
    <svg width="100" height="100" viewBox="0 0 100 100" aria-hidden="true">
      <polygon points="50,6 92,30 8,30" fill="#fff"/>
      <rect x="10" y="34" width="80" height="6" fill="#fff"/>
      <g fill="#fff"><rect x="16" y="44" width="12" height="22"/><rect x="33" y="44" width="12" height="22"/><rect x="55" y="44" width="12" height="22"/><rect x="72" y="44" width="12" height="22"/></g>
      <rect x="8" y="70" width="84" height="8" rx="2" fill="#fff"/>
    </svg>
    <p>National News,<br>Chamber videos,<br>Press Releases</p>
    <div class="cta">CLICK TO VIEW CATEGORY</div>
  </article>
  <article class="market">
    <h2>RELIGIOUS</h2>
    <svg width="100" height="100" viewBox="0 0 100 100" aria-hidden="true" style="left:52px;top:138px">
      <rect x="10" y="40" width="6" height="52" fill="#fff"/><rect x="0" y="52" width="28" height="6" fill="#fff"/>
      <g fill="none" stroke="#fff" stroke-width="4"><polygon points="58,2 74,30 42,30"/><polygon points="58,40 74,12 42,12"/></g>
      <path d="M110 44a24 24 0 1 1-30-22a18 18 0 1 0 30 22Z" fill="#fff"/>
      <circle cx="48" cy="80" r="18" fill="#fff"/>
      <path d="M48 62a9 9 0 0 1 0 18a9 9 0 0 0 0 18a18 18 0 0 1 0-36Z" fill="#1b1d66"/>
    </svg>
    <p>Sermon &amp; Recording</p>
    <div class="cta">CLICK TO VIEW CATEGORY</div>
  </article>
</section>

<section class="lower">
  <h3 style="left:152px;top:30px">About Us:</h3>
  <div class="body-text" style="left:152px;top:56px;width:582px">
    <p>Lorem Ipsum is simply dummy text of the printing and typesetting industry. Lorem Ipsum has been the industry's standard dummy text ever since the 1500s, when an unknown printer took a galley of type and scrambled it to make a type specimen book. It has survived not only five centuries, but also the leap into electronic typesetting, remaining essentially unchanged.</p>
    <p style="margin-top:7px">It was popularised in the 1960s with the release of Letraset sheets containing Lorem Ipsum passages, and more recently with desktop publishing software like Aldus PageMaker including versions of Lorem Ipsum.</p>
  </div>

  <h3 style="left:152px;top:197px">Product Gallery:</h3>
  <div class="thumb" style="left:150px"><span role="img" aria-label="Studio floodlight fixture" style="background:linear-gradient(#e9e9e9,#9a9a9a)"></span></div>
  <div class="thumb" style="left:258px"><span role="img" aria-label="Hanging fluorescent light bank" style="background:linear-gradient(#f2f2f2,#888)"></span></div>
  <div class="thumb" style="left:366px"><span role="img" aria-label="Light kit on stands with case" style="background:linear-gradient(#dcdcdc,#6f6f6f)"></span></div>
  <div class="thumb" style="left:472px"><span role="img" aria-label="Open light fixture housing" style="background:linear-gradient(#f7f3ea,#c9b791)"></span></div>
  <div class="thumb" style="left:581px"><span role="img" aria-label="Slim tube light on tiled floor" style="background:linear-gradient(135deg,#e4e6ea,#a9adb4)"></span></div>
  <div class="view-all">+ View All</div>

  <div class="divider"></div>

  <h3 style="left:806px;top:30px">Contact Us:</h3>
  <div class="body-text" style="left:806px;top:56px;width:300px">
    4810 Linden Park Road, Suite 210<br>Fairview, Ohio 44126<br>Phone: 555-014-2270<br>Fax: 555-014-2271<br>Marketing &amp; Sales – dan.moore@rj7-example.com<br>President – lee.carver@rj7-example.com
  </div>

  <h3 style="left:806px;top:197px">Subscribe to Newsletter:</h3>
  <div class="body-text" style="left:806px;top:219px">Subscribe to our Newsletter &amp; Get Updates:</div>
  <div class="email-field">Enter Email Address...</div>
  <div class="subscribe">SUBSCRIBE<i></i></div>

  <div class="footer-rule"></div>
  <div class="copyright">Copyright © 2012 Bright Harbor Lighting Systems | All Rights Reserved</div>
</section>
</body>
</html>
```